Integrated content management graphic

We are looking for a creative iteration for the attached file. We are currently in the process of renewing our branding and this graphic will be a center piece to our product marketing. Our website is www.brelvonvista.com for more information on products and company.
Future projects are available for designers submitting outstanding concepts and branding capability.
Updates

Project Deadline Extended
Reason: We are in the process of picking our final two.

Target Market(s)

Audience is IT and anyone interested in integrating content management with their ERP/Accounting system.

Industry/Entity Type

Construction

Requirements
Must have
• The design must use the current color scheme associated with our website, yellow, black, grey. White can also be used. The design should be sleek.
Nice to have
• 3D Feel. The wheel could take on a stadium concept in 3d.

```html
<!DOCTYPE html>
<html lang="en">
<head>
<meta charset="utf-8">
<title>Integrated Content Management Wheel</title>
<link href="https://fonts.googleapis.com/css2?family=Arimo:wght@400&display=swap" rel="stylesheet">
<style>
  :root {
    --page: #ffffff;
    --rim-light: #ffffff;
    --rim-shade: #dcdcdc;
    --seg-dark: #464646;
    --seg-mid: #5a5a5a;
    --seg-light: #8c8c8c;
    --seg-hr: #555555;
    --ring-dark: #2b2b2b;
    --ring-inner: #3c3c3c;
    --core: #141414;
    --divider: #1a1a1a;
    --label: #ffffff;
    --accent: #f2d21b;
  }
  html, body {
    margin: 0;
    padding: 0;
    width: 1200px;
    height: 1133px;
    overflow: hidden;
    background: var(--page);
  }
  .wheel {
    display: block;
    width: 1200px;
    height: 1133px;
    font-family: "Arimo", Arial, sans-serif;
  }
  .wheel text { fill: var(--label); }
  .label-outer { font-size: 38px; }
  .label-hr { font-size: 48px; }
  .label-middle { font-size: 25px; }
  .label-inner { font-size: 21px; }
  .core-name { fill: var(--accent) !important; font-size: 22px; }
  .segment { fill: none; }
  .divider { stroke: var(--divider); stroke-width: 4; }
</style>
</head>
<body>
<svg class="wheel" viewBox="0 0 1200 1133" xmlns="http://www.w3.org/2000/svg">
  <defs>
    <radialGradient id="rimGrad" cx="0.5" cy="0.45" r="0.55">
      <stop offset="0.8" stop-color="var(--rim-light)"/>
      <stop offset="1" stop-color="var(--rim-shade)"/>
    </radialGradient>
    <radialGradient id="ringGrad" cx="0.5" cy="0.5" r="0.5">
      <stop offset="0.65" stop-color="#1e1e1e"/>
      <stop offset="0.9" stop-color="#3a3a3a"/>
      <stop offset="1" stop-color="#262626"/>
    </radialGradient>
    <radialGradient id="innerGrad" cx="0.5" cy="0.5" r="0.5">
      <stop offset="0.55" stop-color="#2a2a2a"/>
      <stop offset="1" stop-color="#4a4a4a"/>
    </radialGradient>
    <radialGradient id="coreGrad" cx="0.45" cy="0.4" r="0.6">
      <stop offset="0" stop-color="#3a3a3a"/>
      <stop offset="1" stop-color="var(--core)"/>
    </radialGradient>

    <path id="arc-property" d="M247.4 492.8 A358 358 0 0 1 568.8 198.4"/>
    <path id="arc-project" d="M662.2 202.4 A358 358 0 0 1 956.6 523.8"/>
    <path id="arc-equipment" d="M733.4 921.5 A390 390 0 0 0 990 555"/>
    <path id="arc-facilities" d="M229.1 675.5 A390 390 0 0 0 453.9 916.6"/>

    <path id="arc-office" d="M353.8 511.6 A250 250 0 0 1 539.5 312.4"/>
    <path id="arc-erp" d="M643.4 308.8 A250 250 0 0 1 842.6 494.5"/>
    <path id="arc-pmsoftware" d="M872 559.7 A272 272 0 0 1 576.3 826"/>
    <path id="arc-sharehub" d="M590.5 826.8 A272 272 0 0 1 328.2 564.5"/>
  </defs>

  <!-- base disc -->
  <circle cx="600" cy="555" r="468" fill="url(#rimGrad)"/>

  <!-- outer segments -->
  <g class="outer-ring">
    <circle class="segment" cx="600" cy="555" r="375" pathLength="360" stroke="var(--seg-light)" stroke-width="90" stroke-dasharray="88 272" stroke-dashoffset="89"/>
    <circle class="segment" cx="600" cy="555" r="375" pathLength="360" stroke="var(--seg-mid)" stroke-width="90" stroke-dasharray="69.5 290.5" stroke-dashoffset="-1"/>
    <circle class="segment" cx="600" cy="555" r="375" pathLength="360" stroke="var(--seg-hr)" stroke-width="122" stroke-dasharray="36 324" stroke-dashoffset="-72"/>
    <circle class="segment" cx="600" cy="555" r="375" pathLength="360" stroke="var(--seg-dark)" stroke-width="90" stroke-dasharray="53.5 306.5" stroke-dashoffset="-109.5"/>
    <circle class="segment" cx="600" cy="555" r="375" pathLength="360" stroke="var(--seg-dark)" stroke-width="90" stroke-dasharray="104 256" stroke-dashoffset="-165"/>

    <text class="label-outer"><textPath href="#arc-property" startOffset="50%" text-anchor="middle">Property Mgmt</textPath></text>
    <text class="label-outer"><textPath href="#arc-project" startOffset="50%" text-anchor="middle">Project Mgmt</textPath></text>
    <text class="label-outer"><textPath href="#arc-equipment" startOffset="50%" text-anchor="middle">Equipment Mgmt</textPath></text>
    <text class="label-outer"><textPath href="#arc-facilities" startOffset="50%" text-anchor="middle">Ficilities Mgmt</textPath></text>
    <text class="label-hr" x="600" y="955" text-anchor="middle">HR</text>
  </g>

  <!-- middle ring -->
  <g class="middle-ring">
    <circle cx="600" cy="555" r="302" fill="url(#ringGrad)"/>
    <line class="divider" x1="600" y1="253" x2="600" y2="350"/>
    <line class="divider" x1="902" y1="550" x2="805" y2="552"/>
    <line class="divider" x1="595" y1="857" x2="597" y2="760"/>
    <line class="divider" x1="298" y1="548" x2="395" y2="550"/>

    <text class="label-middle"><textPath href="#arc-office" startOffset="50%" text-anchor="middle">Suite Office</textPath></text>
    <text class="label-middle"><textPath href="#arc-erp" startOffset="50%" text-anchor="middle">ERP</textPath></text>
    <text class="label-middle"><textPath href="#arc-pmsoftware" startOffset="50%" text-anchor="middle">Project Mgmt Software</textPath></text>
    <text class="label-middle"><textPath href="#arc-sharehub" startOffset="50%" text-anchor="middle">ShareHub</textPath></text>
  </g>

  <!-- inner ring -->
  <g class="inner-ring">
    <circle cx="600" cy="555" r="210" fill="#6a6a6a"/>
    <circle cx="600" cy="555" r="206" fill="url(#innerGrad)"/>
    <line class="divider" x1="454.3" y1="409.3" x2="543.4" y2="498.4"/>
    <line class="divider" x1="745.7" y1="409.3" x2="656.6" y2="498.4"/>
    <line class="divider" x1="745.7" y1="700.7" x2="656.6" y2="611.6"/>
    <line class="divider" x1="454.3" y1="700.7" x2="543.4" y2="611.6"/>

    <text class="label-inner" x="592" y="442" text-anchor="middle">Capture</text>
    <text class="label-inner" x="595" y="690" text-anchor="middle">Workfwol</text>
    <text class="label-inner" text-anchor="middle" transform="translate(462 555) rotate(92)">Archiving</text>
    <text class="label-inner" text-anchor="middle" transform="translate(728 560) rotate(80)">
      <tspan x="0" y="-12">Documentary</tspan>
      <tspan x="0" y="14">Managment</tspan>
    </text>
  </g>

  <!-- core -->
  <g class="core">
    <circle cx="600" cy="555" r="84" fill="#4a4a4a"/>
    <circle cx="600" cy="555" r="80" fill="url(#coreGrad)"/>
    <text class="core-name" text-anchor="middle">
      <tspan x="600" y="550">Brelvon</tspan>
      <tspan x="600" y="576">Vista</tspan>
    </text>
  </g>
</svg>
</body>
</html>
```